Adult Literacy Program - flyer to attract volunteers and students

We want a flyer that is engaging, colorful, modern and will appeal to our primary audience of adults aged 40-60. We are trying to attract both prospective volunteers (typically age 50+, mostly women) and students (typically aged 40+).
The flyer should feature diverse people working together in pairs of two, reading or talking, with a workbook or some reading material in front of them.

Our organization trains tutors to work one-on-one with adults who are learning how to read. Most of our adult students are non-native speakers of English. Many are of Haitian or Hispanic origin, so we would like some people who represent that demographic.

The Flyer should represent reading, learning, literacy, knowledge, growth,
and opportunities.
Our students are learning to read so they can advance their job opportunities.

Target Market(s)

Adults aged 40-60, primarily women, retired, volunteers

Industry/Entity Type

Education

Font styles to use
Serif
Sans Serif

Colors

Designer to choose colors to be used in the design.

Requirements
Must have
• - UPDATE: Should be designed as a TRI-FOLD brochure on 8.5 x 11 inch paper that will be folded into thirds.
• - Images of diverse people, women and men, who look Hispanic, Haitian and other nationalities as well as Caucasian.
• - Our logo on the front cover
Nice to have
• The sample flyer is very boring and dry! We are open to different ways of presenting the text.

```html
<!DOCTYPE html>
<html lang="en">
<head>
<meta charset="utf-8">
<title>Volunteer Tutor Tri-Fold Brochure</title>
<link href="https://fonts.googleapis.com/css2?family=Arimo:wght@400;700&display=swap" rel="stylesheet">
<style>
  :root {
    --navy: #0b3b85;
    --mid-blue: #4f86c8;
    --orange: #e07a30;
    --cream: #f3efcf;
    --bullet: #f2e600;
    --white: #ffffff;
    --page: #f4f4f4;
  }
  html, body {
    margin: 0;
    width: 1200px;
    height: 1200px;
    overflow: hidden;
    background: var(--page);
    font-family: "Arimo", Arial, sans-serif;
  }
  .canvas {
    width: 1200px;
    height: 1200px;
    display: flex;
    flex-direction: column;
    align-items: center;
    justify-content: center;
    gap: 22px;
  }
  .spread {
    display: block;
    width: 742px;
    height: 574px;
    box-shadow: 0 4px 14px rgba(0,0,0,0.12);
  }
  .spread text { font-family: "Arimo", Arial, sans-serif; }
  .headline { fill: var(--white); font-weight: 700; font-size: 27px; }
  .contact-title { fill: var(--white); font-weight: 700; font-size: 12.5px; }
  .contact-text { fill: var(--white); font-size: 12.5px; }
  .contact-strong { fill: var(--white); font-size: 12.5px; font-weight: 700; }
  .kicker { fill: var(--orange); font-weight: 700; font-size: 28px; }
  .kicker-sub { fill: var(--white); font-size: 21px; }
  .tagline { fill: var(--white); font-size: 14.5px; }
  .section-title { fill: var(--bullet); font-weight: 700; font-size: 12.5px; }
  .body-text { fill: var(--white); font-size: 11px; }
  .brand-name { fill: var(--navy); font-weight: 700; font-size: 10px; }
  .bullet { fill: var(--bullet); }
  .photo-ring { fill: none; stroke: var(--cream); stroke-width: 8; }
  .white-ring { fill: none; stroke: var(--white); stroke-width: 8; }
  .swoosh { fill: none; stroke: var(--white); stroke-width: 10; stroke-linejoin: round; }
</style>
</head>
<body>
<main class="canvas">

  <!-- Outside spread: back panel, inner flap, front cover -->
  <svg class="spread spread-outside" viewBox="0 0 743 575" xmlns="http://www.w3.org/2000/svg">
    <defs>
      <linearGradient id="coverPhotoTone" x1="0" y1="0" x2="1" y2="1">
        <stop offset="0" stop-color="#8fb3a6"/>
        <stop offset="0.5" stop-color="#c9a58a"/>
        <stop offset="1" stop-color="#7a5138"/>
      </linearGradient>
      <linearGradient id="classroomTone" x1="0" y1="0" x2="1" y2="1">
        <stop offset="0" stop-color="#b9b4a8"/>
        <stop offset="1" stop-color="#5b6f86"/>
      </linearGradient>
      <linearGradient id="pairTone" x1="0" y1="0" x2="1" y2="1">
        <stop offset="0" stop-color="#c7c2b0"/>
        <stop offset="1" stop-color="#4d7a7c"/>
      </linearGradient>
    </defs>

    <rect class="panel-base" width="743" height="575" fill="var(--mid-blue)"/>

    <!-- Back panel -->
    <rect x="0" y="270" width="243" height="305" fill="var(--navy)"/>
    <text class="headline" x="20" y="70">DON’T</text>
    <text class="headline" x="20" y="104">WASTE A</text>
    <text class="headline" x="20" y="138">MOMENT !</text>

    <text class="contact-title" x="25" y="344">CONTACT US TODAY</text>
    <text class="contact-title" x="25" y="360">TO LEARN MORE.</text>
    <text class="contact-text" x="25" y="392">Volunteer Desk:</text>
    <text class="contact-strong" x="25" y="408">555-014-7510</text>
    <text class="contact-text" x="25" y="439">Lakeside,</text>
    <text class="contact-text" x="25" y="455">Millbrook &amp; South Bend:</text>
    <text class="contact-strong" x="25" y="471">555-014-3453</text>
    <text class="contact-text" x="25" y="503">email: tutors@pagepartners.org</text>

    <!-- Cover photo area -->
    <path role="img" aria-label="Photo of a smiling young woman holding a notebook, classmates blurred behind her"
          d="M228,0 H743 V470 C660,445 600,425 520,395 C420,355 330,305 290,245 C250,185 235,90 228,0 Z"
          fill="url(#coverPhotoTone)"/>
    <path class="swoosh" d="M228,0 C235,90 250,185 290,245 C330,305 420,355 520,395 C600,425 660,445 743,470"/>

    <!-- Logo roundel -->
    <circle cx="370" cy="83" r="66" fill="var(--white)"/>
    <text class="brand-name" x="370" y="80" text-anchor="middle">PAGE PARTNERS</text>
    <text class="brand-name" x="370" y="94" text-anchor="middle">LITERACY</text>

    <!-- Photo circles -->
    <circle role="img" aria-label="Photo of a tutor crouching beside learners in a classroom" cx="246" cy="191" r="71" fill="url(#classroomTone)"/>
    <circle class="photo-ring" cx="246" cy="191" r="71"/>
    <circle role="img" aria-label="Photo of two women studying a workbook together at a table" cx="495" cy="385" r="105" fill="url(#pairTone)"/>
    <circle class="photo-ring" cx="495" cy="385" r="105"/>

    <text class="kicker" x="616" y="37" text-anchor="middle">VOLUNTEER</text>
    <text class="kicker-sub" x="616" y="64" text-anchor="middle">ENRICH A LIFE!</text>

    <rect x="493" y="500" width="250" height="75" fill="var(--navy)"/>
    <text class="tagline" x="619" y="530" text-anchor="middle">Help an adult learn to read,</text>
    <text class="tagline" x="619" y="548" text-anchor="middle">write or speak English</text>
  </svg>

  <!-- Inside spread: tutors, students -->
  <svg class="spread spread-inside" viewBox="0 0 743 575" xmlns="http://www.w3.org/2000/svg">
    <defs>
      <linearGradient id="tutorPairTone" x1="0" y1="0" x2="1" y2="1">
        <stop offset="0" stop-color="#d9d3c8"/>
        <stop offset="0.5" stop-color="#b08c72"/>
        <stop offset="1" stop-color="#e59a7c"/>
      </linearGradient>
      <linearGradient id="studentsTone" x1="0" y1="0" x2="1" y2="1">
        <stop offset="0" stop-color="#a06650"/>
        <stop offset="1" stop-color="#d8c96a"/>
      </linearGradient>
      <clipPath id="insideClip"><rect width="743" height="575"/></clipPath>
    </defs>

    <rect width="743" height="575" fill="var(--mid-blue)"/>

    <!-- Tutoring pair photo -->
    <path role="img" aria-label="Photo of an older man and a woman working through a workbook with a pencil"
          d="M249,0 H743 V460 C600,360 420,350 310,315 C255,297 258,242 330,230 C410,218 485,212 460,180 C420,130 300,90 249,0 Z"
          fill="url(#tutorPairTone)"/>
    <path class="swoosh" d="M249,0 C300,90 420,130 460,180 C485,212 410,218 330,230 C258,242 255,297 310,315 C420,350 600,360 743,460"/>

    <!-- Tutors panel -->
    <rect x="0" y="47" width="248" height="253" fill="var(--navy)"/>
    <text class="section-title" x="17" y="109">TUTORS</text>
    <g class="tutor-list">
      <circle class="bullet" cx="18" cy="135" r="4.5"/>
      <text class="body-text" x="26" y="139">No special skills or degrees</text>
      <text class="body-text" x="26" y="152">needed — just a degree of caring!</text>
      <circle class="bullet" cx="18" cy="162" r="4.5"/>
      <text class="body-text" x="26" y="166">Training offered throughout the year</text>
      <circle class="bullet" cx="18" cy="175" r="4.5"/>
      <text class="body-text" x="26" y="179">Tutors meet students weekly at a library</text>
      <circle class="bullet" cx="18" cy="188" r="4.5"/>
      <text class="body-text" x="26" y="192">Instructional materials provided</text>
      <circle class="bullet" cx="18" cy="202" r="4.5"/>
      <text class="body-text" x="26" y="206">Ongoing support available</text>
    </g>
    <text class="body-text" x="20" y="233">Teach an adult to read and you’ll</text>
    <text class="body-text" x="20" y="246">change a life forever.</text>

    <text class="kicker" x="614" y="40" text-anchor="middle">VOLUNTEER</text>
    <text class="kicker-sub" x="614" y="67" text-anchor="middle">ENRICH A LIFE!</text>

    <!-- Students photo circle -->
    <g clip-path="url(#insideClip)">
      <circle role="img" aria-label="Photo of two smiling students outdoors, one holding binders" cx="115" cy="470" r="114" fill="url(#studentsTone)"/>
      <circle class="white-ring" cx="115" cy="470" r="114"/>
    </g>

    <!-- Students panel -->
    <rect x="251" y="340" width="250" height="235" fill="var(--navy)"/>
    <text class="section-title" x="269" y="373">STUDENTS</text>
    <text class="body-text" x="275" y="401">Students are adults in need of :</text>
    <g class="student-list">
      <circle class="bullet" cx="265" cy="424" r="4.5"/>
      <text class="body-text" x="275" y="428">basic literacy skills</text>
      <circle class="bullet" cx="265" cy="437" r="4.5"/>
      <text class="body-text" x="275" y="441">pre-GED skills</text>
      <circle class="bullet" cx="265" cy="451" r="4.5"/>
      <text class="body-text" x="275" y="455">conversational English</text>
      <circle class="bullet" cx="265" cy="464" r="4.5"/>
      <text class="body-text" x="275" y="468">Tutoring is free of charge</text>
      <circle class="bullet" cx="265" cy="478" r="4.5"/>
      <text class="body-text" x="275" y="482">Tutoring is one-on-one</text>
      <circle class="bullet" cx="265" cy="491" r="4.5"/>
      <text class="body-text" x="275" y="495">Flexible scheduling during library hours</text>
      <circle class="bullet" cx="265" cy="505" r="4.5"/>
      <text class="body-text" x="275" y="509">Lessons focus on student goals</text>
    </g>
    <text class="body-text" x="272" y="540">IF YOU CAN READ, YOU CAN TUTOR!</text>

    <!-- Logo roundel -->
    <circle cx="616" cy="493" r="58" fill="var(--white)"/>
    <text class="brand-name" x="616" y="490" text-anchor="middle">PAGE PARTNERS</text>
    <text class="brand-name" x="616" y="504" text-anchor="middle">LITERACY</text>
  </svg>

</main>
</body>
</html>
```